Private Equity Fund needs a powerpoint template

We need a power point presentation template for our recent founded firm, Corvane Partners, a private equity/investment fund (funded by investors, is a firm that buys, holds and sells companies years after) focused in turnaround cases. The presentation should address corporate and financial subjects in a clean/plain way, but as most straightforward way as possible. This is a commercial pitch/flip presentation, is not a presentation with animations to be presented to a mass of people.

We would like that the designer resume the file that we began building (adapted from other funds/advisors of the market) and establish the following according to our logo:
1) a new set of fonts (size levels and type),
2) colors (tables, headers, lines),
3) space available for content (text boxes, tables, pictures or charts) (note left column space in blank)
4) set, our Excel applications to use as default, the color guide that you have you defined
5) white background

Basically, we need to change the items listed above to the "Example.ppt" file uploaded along with those instructions.

The presentation should:
A) rule how the people in our organization should address our messages (guide with size of tables, font and size, colors)
B) pattern a set of slides that could minimize the time for arranging formats, worrying only about the content
C) allow the person who is building the presentation to have options while addressing the message

Dont get too restricted to what we are giving you (the "Example.ppt" file). You may suggest:
i) logo positioning
ii) with or without any vague space (left column space in blank)
iii) space optmization
iv) shades and colors
v) fonts (careful with the wide ones as it does not optimizes space)

I'm uploading:

Target Market(s)

Banks
Investors
Company owners/founders
Funds

Industry/Entity Type

Financial Service

Font styles to use
Other font styles liked:
• Arial Narrow, Arial, trojan

Colors

Designer to choose colors to be used in the design.

Requirements
Must have
• We would like that the designer resume the file that we began building (adapted from other funds/advisors of the market) and establish the following according to our logo:
• 1) a new set of fonts (size levels and type),
• 2) colors (tables, headers, lines),
• 3) space available for content (text boxes, tables, pictures or charts) (note left column space in blank)
• 4) set, our Excel applications to use as default, the color guide that you have you defined
• 5) white background
Nice to have
• Narrow font type
• Space optimization
• Discrete
Should not have
• Animations
• Font size too big
• colored background

```html
<!DOCTYPE html>
<html lang="en">
<head>
<meta charset="utf-8">
<title>Corvane Partners – Content Slide</title>
<link href="https://fonts.googleapis.com/css2?family=IM+Fell+English+SC&family=Lato:wght@400;700&display=swap" rel="stylesheet">
<style>
  :root {
    --ink: #111111;
    --body: #2e2e2e;
    --rule: #555555;
    --footer-bg: #333333;
    --footer-ink: #f2f2f2;
    --mark: #3a3a3a;
    --paper: #ffffff;
  }
  html, body {
    margin: 0;
    padding: 0;
    width: 1200px;
    height: 900px;
    overflow: hidden;
    background: var(--paper);
  }
  .slide {
    position: relative;
    width: 1200px;
    height: 900px;
    background: var(--paper);
    font-family: "Lato", Arial, sans-serif;
    color: var(--body);
  }
  .slide-title {
    position: absolute;
    left: 30px;
    top: 26px;
    margin: 0;
    font-family: "IM Fell English SC", "Times New Roman", serif;
    font-weight: 400;
    font-size: 46px;
    letter-spacing: 1px;
    color: var(--ink);
    line-height: 1.2;
  }
  .title-rule {
    position: absolute;
    left: 0;
    top: 85px;
    width: 570px;
    height: 1.5px;
    background: var(--rule);
  }
  .brand {
    position: absolute;
    right: 26px;
    top: 30px;
    display: flex;
    align-items: center;
    gap: 14px;
  }
  .brand-square {
    width: 48px;
    height: 48px;
    background: var(--mark);
  }
  .brand-name {
    font-family: "Lato", Arial, sans-serif;
    font-weight: 400;
    font-size: 34px;
    color: var(--mark);
    line-height: 1;
  }
  .content-block {
    position: absolute;
    width: 500px;
  }
  .content-block h2 {
    margin: 0;
    font-size: 27px;
    font-weight: 700;
    line-height: 32px;
    color: var(--ink);
  }
  .content-block p {
    margin: 4px 0 0;
    font-size: 20.5px;
    line-height: 37.5px;
    color: var(--body);
  }
  .block-left-top { left: 66px; top: 159px; }
  .block-right-top { left: 684px; top: 153px; }
  .block-left-bottom { left: 66px; top: 497px; }
  .block-right-bottom { left: 684px; top: 491px; }
  .footer {
    position: absolute;
    left: 0;
    bottom: 0;
    width: 1200px;
    height: 61px;
    background: var(--footer-bg);
    color: var(--footer-ink);
    font-size: 21px;
    display: flex;
    align-items: center;
    justify-content: space-between;
    padding: 0 18px 0 15px;
    box-sizing: border-box;
  }
</style>
</head>
<body>
<main class="slide">
  <h1 class="slide-title">PROJECT TITLE HERE</h1>
  <div class="title-rule"></div>

  <div class="brand">
    <div class="brand-square"></div>
    <span class="brand-name">Corvane Partners</span>
  </div>

  <section class="content-block block-left-top">
    <h2>Subtext Title Here</h2>
    <p>Lorem ipsum data sit Lorem ipsum data sit Lorem<br>ipsum data sit Lorem ipsum data sit Lorem ipsum<br>data sit Lorem ipsum data sit Lorem ipsum data sit<br>Lorem ipsum data sit Lorem ipsum data sit Lorem<br>ipsum data sit Lorem ipsum data sit Lorem ipsum<br>data sit Lorem ipsum data sit Lorem ipsum data sit<br>Lorem ipsum data sit Lorem ipsum data sit</p>
  </section>

  <section class="content-block block-right-top">
    <h2>Subtext Title Here</h2>
    <p>Lorem ipsum data sit Lorem ipsum data sit Lorem<br>ipsum data sit Lorem ipsum data sit Lorem ipsum<br>data sit Lorem ipsum data sit Lorem ipsum data sit<br>Lorem ipsum data sit Lorem ipsum data sit Lorem<br>ipsum data sit Lorem ipsum data sit Lorem ipsum<br>data sit Lorem ipsum data sit Lorem ipsum data sit<br>Lorem ipsum data sit Lorem ipsum data sit</p>
  </section>

  <section class="content-block block-left-bottom">
    <h2>Subtext Title Here</h2>
    <p>Lorem ipsum data sit Lorem ipsum data sit Lorem<br>ipsum data sit Lorem ipsum data sit Lorem ipsum<br>data sit Lorem ipsum data sit Lorem ipsum data sit<br>Lorem ipsum data sit Lorem ipsum data sit Lorem<br>ipsum data sit Lorem ipsum data sit Lorem ipsum<br>data sit Lorem ipsum data sit Lorem ipsum data sit<br>Lorem ipsum data sit Lorem ipsum data sit</p>
  </section>

  <section class="content-block block-right-bottom">
    <h2>Subtext Title Here</h2>
    <p>Lorem ipsum data sit Lorem ipsum data sit Lorem<br>ipsum data sit Lorem ipsum data sit Lorem ipsum<br>data sit Lorem ipsum data sit Lorem ipsum data sit<br>Lorem ipsum data sit Lorem ipsum data sit Lorem<br>ipsum data sit Lorem ipsum data sit Lorem ipsum<br>data sit Lorem ipsum data sit Lorem ipsum data sit<br>Lorem ipsum data sit Lorem ipsum data sit</p>
  </section>

  <footer class="footer">
    <span class="footer-copyright">Copyrigh text here</span>
    <span class="footer-page">Page : 02</span>
  </footer>
</main>
</body>
</html>
```